Need new website for my business

I want to design a new Irrigation website for our business. What we are looking for is to have a residential section that describes providing for irrigation service for residential customers in homeowners Association. From startups to service to winterization in full residential installs.
A commercial section on our webpage describing. installation of commercial Irrigation systems. Service start-up of systems. To winterizations. Offering contract service plans for commercial customers.
Service for both commercial residential include making sure all zones are operating check for leaks adjust spray nozzles in rotors making sure all irrigation heads rotate, and are not stuck or damaged making sure that we have full coverage of each Irrigation zone for lawns. In all drip irrigation is Functioning in watering the plants accordingly. Adjusting control settings to make sure you have the right watering times during the hot dry months.
Have a landscape lighting tab:
Describing what landscape lighting and what it does to enhance curb, appeal, highlight architectural, features of landscape and transferring your outdoor space into inviting visual stunning areas with low-voltage landscape lighting
And a residential snow plowing for the Falmouth Maine area. In commercial snow, plowing and snow removal covering Scarborough south portland Portland Falmouth in Cumberland Maine for commercial Snow services. From plow & Salting parking lots to Snow removing, and Snow displacement.
we started a website but it needs a up lift and bring it to pop
our web site is willowbrookyards314.com
here are a few websites that we really like:
www.sprinklecoastal.com
www.dewpointwatering.com
www.verdantlawnsystems.com
Industry/Entity Type
Irrigation & Landscape Lighting
Coding
Coded - Design and coding required
Number of Pages Required
4 page

```html
<!DOCTYPE html>
<html lang="en">
<head>
<meta charset="utf-8">
<title>Willowbrook Yards – Irrigation, Landscape Lighting & Snow Service</title>
<link rel="stylesheet" href="https://fonts.googleapis.com/css2?family=Comfortaa:wght@500;600;700&family=Poppins:wght@400;500;600;700&family=Dancing+Script:wght@500&display=swap">
<style>
:root{
  --blue:#1a87d0;
  --blue-dark:#0f5f9e;
  --green:#17972b;
  --green-dark:#0b6d2a;
  --ink:#1d1d1d;
  --text:#444;
  --muted:#777;
  --footer:#2a2a2a;
  --line:#e3e3e3;
  --star:#f26a1b;
}
*{box-sizing:border-box;margin:0;padding:0}
html,body{width:1200px;height:4570px;overflow:hidden}
body{font-family:"Poppins",sans-serif;color:var(--text);background:#fff;position:relative}
.abs{position:absolute}
.btn{position:absolute;display:flex;align-items:center;justify-content:center;gap:6px;border-radius:22px;color:#fff;font-size:13px;font-weight:500}
.btn-blue{background:var(--blue)}
.btn-green{background:var(--green)}

/* header */
.site-header{position:absolute;top:0;left:0;width:1200px;height:84px;background:#fff}
.brand{position:absolute;left:71px;top:22px;display:flex;align-items:center;gap:10px}
.brand-dot{width:22px;height:22px;border-radius:50%;background:var(--green)}
.brand-name{font-family:"Poppins",sans-serif;font-weight:700;font-size:26px;color:var(--green);line-height:1}
.brand-sub{position:absolute;left:71px;top:58px;font-size:10px;color:var(--blue)}
.nav a{position:absolute;top:31px;font-size:13px;color:#333;text-decoration:none}
.nav .active{color:var(--blue)}
.nav .contact-btn{top:23px;left:1030px;width:99px;height:37px;border-radius:19px;background:var(--blue);color:#fff;display:flex;align-items:center;justify-content:center}

/* hero */
.hero{position:absolute;top:84px;left:0;width:1200px;height:544px;background:linear-gradient(100deg,#15191a 0%,#273126 45%,#3f5a2e 70%,#6d6a4d 100%)}
.hero h1{position:absolute;left:71px;top:124px;font-family:"Comfortaa",sans-serif;font-weight:500;font-size:39px;line-height:52px;color:#fff}
.hero p{position:absolute;left:71px;top:282px;width:450px;font-size:14px;line-height:23px;color:#fff}

/* about */
.photo{position:absolute;background:linear-gradient(135deg,#2f4a22,#6d8a3e)}
.badge{position:absolute;left:318px;top:890px;width:120px;height:120px;border-radius:50%;background:#fff;display:flex;flex-direction:column;align-items:center;justify-content:center;text-align:center}
.badge strong{font-family:"Comfortaa",sans-serif;font-size:31px;color:var(--blue);font-weight:600;line-height:1}
.badge span{font-size:11px;color:#222;line-height:14px;margin-top:6px;font-weight:500}
.eyebrow{font-size:13px;color:var(--blue)}
.about-title{position:absolute;left:669px;top:740px;font-family:"Comfortaa",sans-serif;font-weight:600;font-size:32px;line-height:39px;color:#111}
.about-text{position:absolute;left:670px;top:910px;width:392px;font-size:12.6px;line-height:20.4px;color:#333}

/* section titles */
.sec-title{position:absolute;left:0;width:1200px;text-align:center;font-weight:700;font-size:32px;color:var(--green)}
.sec-rule{position:absolute;left:573px;width:54px;height:3px;background:var(--blue)}
.sec-sub{position:absolute;left:0;width:1200px;text-align:center;font-size:13px;color:#333}

/* services */
.service-card{position:absolute;border-radius:14px;overflow:hidden}
.service-card .label{position:absolute;left:23px;bottom:27px;color:#fff;font-weight:600;font-size:16px}
.service-card .go{position:absolute;right:24px;bottom:22px;width:30px;height:30px;border:1.5px solid #fff;border-radius:50%;display:flex;align-items:center;justify-content:center}

/* areas */
.map-area{position:absolute;left:0;top:2024px;width:600px;height:576px;background:linear-gradient(160deg,#e6efe3 0%,#dfe9dc 45%,#a9d3ec 70%,#9fcde9 100%)}
.areas{position:absolute;left:600px;top:2024px;width:600px;height:576px;background:linear-gradient(120deg,#129a3b 0%,#0f8a34 55%,#1d6f3b 100%)}
.areas h2{position:absolute;left:57px;top:82px;font-weight:600;font-size:32px;line-height:45px;color:#fff}
.areas .rule{position:absolute;left:57px;top:184px;width:54px;height:3px;background:#fff}
.zip{position:absolute;left:57px;top:216px;width:355px;height:43px;border-radius:22px;background:#fff;font-size:12px;color:#333;padding:13px 0 0 25px}
.zip i{position:absolute;right:8px;top:7px;width:29px;height:29px;border-radius:50%;background:var(--green);display:flex;align-items:center;justify-content:center}
.town{position:absolute;display:flex;align-items:center;gap:9px;font-size:14px;color:#fff}
.areas .note{position:absolute;left:57px;top:434px;font-size:12.5px;color:#fff}
.areas .call{position:absolute;left:57px;top:464px;font-size:16px;color:#fff;display:flex;align-items:center;gap:6px}

/* reviews */
.review{position:absolute;top:2801px;width:285px;height:323px;background:#fff;border-radius:8px;box-shadow:0 4px 18px rgba(0,0,0,.08)}
.review p{position:absolute;left:24px;top:30px;width:242px;font-size:11.3px;line-height:21.5px;color:#444}
.review .who{position:absolute;left:26px;top:180px;font-weight:700;font-size:14px;color:var(--green)}
.review .src{position:absolute;left:26px;top:200px;font-size:11px;color:#555}
.review .line{position:absolute;left:0;top:250px;width:285px;height:1px;background:var(--line)}
.review .src-dot{position:absolute;left:125px;top:234px;width:32px;height:32px;border-radius:50%;background:#fff;box-shadow:0 2px 6px rgba(0,0,0,.15);display:flex;align-items:center;justify-content:center}
.review .src-dot b{width:14px;height:14px;border-radius:50%;background:#c9c9c9}
.review .rated{position:absolute;left:24px;top:283px;font-size:13px;color:#333}
.review .stars{position:absolute;right:25px;top:283px;color:var(--star);font-size:13px;letter-spacing:2px}
.arrow{position:absolute;top:2938px}

/* cta */
.cta{position:absolute;top:3218px;left:0;width:1200px;height:346px;background:linear-gradient(100deg,#1a73c0 0%,#1677c4 50%,#16608f 100%)}
.cta h2{position:absolute;left:0;width:1200px;top:76px;text-align:center;font-weight:600;font-size:31px;color:#fff}
.cta p{position:absolute;left:230px;width:740px;top:136px;text-align:center;font-size:16px;line-height:28px;color:#fff}
.cta .call-btn{position:absolute;left:483px;top:220px;width:232px;height:39px;border:1.5px solid #fff;border-radius:20px;color:#fff;font-size:12.5px;display:flex;align-items:center;justify-content:center;gap:6px}

/* contact */
.script{position:absolute;left:142px;top:3664px;font-family:"Dancing Script",cursive;font-size:30px;color:var(--blue)}
.contact-title{position:absolute;left:142px;top:3695px;font-weight:700;font-size:31px;color:var(--green)}
.contact-sub{position:absolute;left:142px;top:3739px;font-size:12px;color:#333}
.c-item{position:absolute;left:140px}
.c-icon{position:absolute;left:0;top:0;width:68px;height:68px;border-radius:50%;background:#fff;box-shadow:0 3px 14px rgba(0,0,0,.1);display:flex;align-items:center;justify-content:center}
.c-item h4{position:absolute;left:89px;top:6px;font-weight:500;font-size:17px;color:#222;white-space:nowrap}
.c-item span{position:absolute;left:89px;top:36px;width:250px;font-size:11.5px;line-height:22px;color:#333}
.form-card{position:absolute;left:609px;top:3651px;width:451px;height:541px;background:#fff;border-top:4px solid var(--green);border-radius:6px;box-shadow:0 6px 24px rgba(0,0,0,.12);z-index:2}
.form-card h3{position:absolute;left:27px;top:34px;font-weight:700;font-size:31px;color:var(--green)}
.field{position:absolute;left:27px;width:396px;height:60px;border-bottom:1px solid var(--line)}
.field label{position:absolute;left:0;top:0;font-size:12px;color:#222;font-weight:500}
.field span{position:absolute;left:0;top:27px;font-size:12px;color:#999}
.field svg{position:absolute;right:0;top:27px}

/* footer */
.footer{position:absolute;top:4109px;left:0;width:1200px;height:461px;background:var(--footer)}
.f-brand{position:absolute;left:142px;top:156px;display:flex;align-items:center;gap:10px}
.f-brand .brand-name{color:#fff;font-size:26px;font-weight:700}
.f-brand-sub{position:absolute;left:142px;top:192px;font-size:10px;color:#ddd}
.f-about{position:absolute;left:142px;top:220px;width:285px;font-size:11.5px;line-height:21.5px;color:#eee}
.f-col{position:absolute;top:150px}
.f-col h5{font-weight:600;font-size:16px;color:#fff;margin-bottom:16px}
.f-col li{list-style:none;font-size:11.5px;color:#eee;line-height:27px}
.f-social li{display:flex;align-items:center;gap:12px;line-height:36px;font-size:12px}
.f-social .ico{width:26px;height:26px;border-radius:50%;border:1.5px solid #fff}
.f-social .ico.solid{background:var(--green);border-color:var(--green)}
.f-rule{position:absolute;left:142px;top:399px;width:916px;height:1px;background:#4a4a4a}
.copy{position:absolute;left:0;width:1200px;top:424px;text-align:center;font-size:11.5px;color:#eee}
</style>
</head>
<body>

<header class="site-header">
  <div class="brand"><div class="brand-dot"></div><div class="brand-name">willowbrook</div></div>
  <div class="brand-sub">Landscape &amp; Landscape Lighting &amp; Irrigation</div>
  <nav class="nav">
    <a class="active" style="left:486px">Home</a>
    <a style="left:560px">Irrigation</a>
    <a style="left:654px">Landscape Lighting</a>
    <a style="left:814px">Snow Plowing</a>
    <a style="left:938px">About Us</a>
    <a class="contact-btn">Contact Us</a>
  </nav>
</header>

<section class="hero" role="img" aria-label="Night photograph of lit garden steps with planters and trees strung with lights">
  <h1>Irrigation System,<br>Landscape Lighting,<br>Residential Snow Service</h1>
  <p>Our team of experienced landscape property maintenance professionals is dedicated to enhancing the beauty and functionality of your property.</p>
  <div class="btn btn-blue" style="left:71px;top:374px;width:176px;height:40px">Get Started Now
    <svg width="12" height="12" viewBox="0 0 12 12"><path d="M1 6h9M6 2l4 4-4 4" stroke="#fff" stroke-width="1.5" fill="none"/></svg></div>
  <div class="btn btn-green" style="left:261px;top:374px;width:204px;height:40px">Explore Our Services
    <svg width="12" height="12" viewBox="0 0 12 12"><path d="M1 6h9M6 2l4 4-4 4" stroke="#fff" stroke-width="1.5" fill="none"/></svg></div>
</section>

<section class="about">
  <div class="photo" style="left:142px;top:714px;width:225px;height:223px;border-radius:30px 0 0 0" role="img" aria-label="Garden path with clipped shrubs lit at dusk"></div>
  <div class="photo" style="left:387px;top:714px;width:227px;height:223px;background:linear-gradient(135deg,#2c2212,#7a5a2a)" role="img" aria-label="Bollard light glowing beside a planted bed"></div>
  <div class="photo" style="left:142px;top:960px;width:225px;height:226px;background:linear-gradient(135deg,#1e2a1a,#55704a)" role="img" aria-label="Sprinkler spray over grasses"></div>
  <div class="photo" style="left:387px;top:960px;width:227px;height:226px;border-radius:0 0 40px 0;background:linear-gradient(135deg,#3d7a22,#8fbf3a)" role="img" aria-label="Red lawn mower on fresh-cut grass"></div>
  <div class="badge"><strong>25+</strong><span>YEARS OF<br>EXPERIENCE</span></div>

  <div class="abs eyebrow" style="left:669px;top:716px">About Willowbrook Yards</div>
  <h2 class="about-title">Experienced<br>Landscape &amp; Property<br>Maintenance Team</h2>
  <svg class="abs" style="left:669px;top:872px" width="72" height="20" viewBox="0 0 72 20"><circle cx="10" cy="10" r="8" fill="none" stroke="var(--green)" stroke-width="2.5"/><line x1="32" y1="10" x2="70" y2="10" stroke="var(--green)" stroke-width="2.5"/></svg>
  <p class="about-text">Our team of experienced landscape property maintenance professionals is dedicated to enhancing the beauty and functionality of your property. With a keen eye for detail, we provide tailored maintenance services in the residential and commercial sectors that include lawn care, irrigation services, landscape lighting, design and installation, residential snow services and more. Whether you're looking to keep your property pristine year-round or need seasonal services, our team combines expertise and creativity to exceed your expectation.</p>
  <div class="btn btn-blue" style="left:669px;top:1141px;width:233px;height:39px">Schedule A Consultation
    <svg width="12" height="12" viewBox="0 0 12 12"><path d="M1 6h9M6 2l4 4-4 4" stroke="#fff" stroke-width="1.5" fill="none"/></svg></div>
</section>

<section class="services">
  <h2 class="sec-title" style="top:1298px">Professional Services</h2>
  <div class="sec-rule" style="top:1352px"></div>
  <p class="sec-sub" style="top:1376px">Comprehensive outdoor solutions for residential and commercial properties throughout Southern Maine</p>

  <div class="service-card" style="left:142px;top:1415px;width:600px;height:250px;background:linear-gradient(180deg,#7c8a6c 0%,#3f6a2a 55%,#1f3a16 100%)" role="img" aria-label="Sprinklers watering a green residential lawn">
    <div class="label">Residential Irrigation Systems</div>
    <div class="go"><svg width="12" height="12" viewBox="0 0 12 12"><path d="M2 10L10 2M4 2h6v6" stroke="#fff" stroke-width="1.4" fill="none"/></svg></div></div>
  <div class="service-card" style="left:761px;top:1415px;width:297px;height:250px;background:linear-gradient(180deg,#12202a 0%,#1f3f56 50%,#223018 100%)" role="img" aria-label="Lit pool and garden at night">
    <div class="label">Landscape Lighting</div>
    <div class="go"><svg width="12" height="12" viewBox="0 0 12 12"><path d="M2 10L10 2M4 2h6v6" stroke="#fff" stroke-width="1.4" fill="none"/></svg></div></div>
  <div class="service-card" style="left:142px;top:1683px;width:295px;height:248px;background:linear-gradient(180deg,#b9bcbd 0%,#8e9396 55%,#4b4f4f 100%)" role="img" aria-label="Loader clearing snow on a street">
    <div class="label">Snow Removal Services</div>
    <div class="go"><svg width="12" height="12" viewBox="0 0 12 12"><path d="M2 10L10 2M4 2h6v6" stroke="#fff" stroke-width="1.4" fill="none"/></svg></div></div>
  <div class="service-card" style="left:456px;top:1683px;width:602px;height:248px;background:linear-gradient(180deg,#b5c4c6 0%,#6b9a7a 50%,#1f4f26 100%)" role="img" aria-label="Overhead irrigation inside a commercial greenhouse">
    <div class="label">Commercial Irrigation Systems</div>
    <div class="go"><svg width="12" height="12" viewBox="0 0 12 12"><path d="M2 10L10 2M4 2h6v6" stroke="#fff" stroke-width="1.4" fill="none"/></svg></div></div>
</section>

<div class="map-area" role="img" aria-label="Map of the Portland, Maine service area"></div>
<section class="areas">
  <h2>Serving Southern<br>Maine Communities</h2>
  <div class="rule"></div>
  <div class="zip">Enter Zip code<i><svg width="14" height="14" viewBox="0 0 14 14"><circle cx="6" cy="6" r="4.2" stroke="#fff" stroke-width="1.6" fill="none"/><path d="M9 9l3.5 3.5" stroke="#fff" stroke-width="1.6"/></svg></i></div>
  <div class="town" style="left:57px;top:296px"><svg width="12" height="16" viewBox="0 0 12 16"><path d="M6 0a6 6 0 0 1 6 6c0 4.5-6 10-6 10S0 10.5 0 6a6 6 0 0 1 6-6z" fill="#fff"/><circle cx="6" cy="6" r="2.2" fill="#129a3b"/></svg>Portland</div>
  <div class="town" style="left:222px;top:296px"><svg width="12" height="16" viewBox="0 0 12 16"><path d="M6 0a6 6 0 0 1 6 6c0 4.5-6 10-6 10S0 10.5 0 6a6 6 0 0 1 6-6z" fill="#fff"/><circle cx="6" cy="6" r="2.2" fill="#129a3b"/></svg>South Portland</div>
  <div class="town" style="left:57px;top:337px"><svg width="12" height="16" viewBox="0 0 12 16"><path d="M6 0a6 6 0 0 1 6 6c0 4.5-6 10-6 10S0 10.5 0 6a6 6 0 0 1 6-6z" fill="#fff"/><circle cx="6" cy="6" r="2.2" fill="#129a3b"/></svg>Scarborough</div>
  <div class="town" style="left:222px;top:337px"><svg width="12" height="16" viewBox="0 0 12 16"><path d="M6 0a6 6 0 0 1 6 6c0 4.5-6 10-6 10S0 10.5 0 6a6 6 0 0 1 6-6z" fill="#fff"/><circle cx="6" cy="6" r="2.2" fill="#129a3b"/></svg>Falmouth</div>
  <div class="town" style="left:57px;top:379px"><svg width="12" height="16" viewBox="0 0 12 16"><path d="M6 0a6 6 0 0 1 6 6c0 4.5-6 10-6 10S0 10.5 0 6a6 6 0 0 1 6-6z" fill="#fff"/><circle cx="6" cy="6" r="2.2" fill="#129a3b"/></svg>Cumberland</div>
  <div class="town" style="left:222px;top:379px"><svg width="12" height="16" viewBox="0 0 12 16"><path d="M6 0a6 6 0 0 1 6 6c0 4.5-6 10-6 10S0 10.5 0 6a6 6 0 0 1 6-6z" fill="#fff"/><circle cx="6" cy="6" r="2.2" fill="#129a3b"/></svg>Surrounding Areas</div>
  <p class="note">If you don't see your location listed above,</p>
  <p class="call">please contact us at <svg width="15" height="15" viewBox="0 0 16 16"><path d="M3 1l3 3-2 2c1 2 3 4 5 5l2-2 3 3-2 3C7 15 1 9 1 3z" fill="none" stroke="#fff" stroke-width="1.4"/></svg>(123) 456-7890</p>
</section>

<section class="reviews">
  <h2 class="sec-title" style="top:2683px">What Our Clients Say</h2>
  <div class="sec-rule" style="top:2737px"></div>
  <p class="sec-sub" style="top:2758px">Trusted by homeowners and businesses throughout Southern Maine</p>
  <svg class="arrow" style="left:66px" width="24" height="46" viewBox="0 0 24 46"><path d="M22 2L3 23l19 21" stroke="#2a7fc4" stroke-width="1.8" fill="none"/></svg>
  <svg class="arrow" style="left:1110px" width="24" height="46" viewBox="0 0 24 46"><path d="M2 2l19 21L2 44" stroke="#2a7fc4" stroke-width="1.8" fill="none"/></svg>

  <div class="review" style="left:142px"><p>Ut wisi enim ad minim venia quis nostrud exerci tation ullamcorper suscipit lobortis nisl ut aliquip ex ea commodo consequat. Duis autem vel eum ire dolor in hendrerit in vulputate velit esse molesti consequat, vel illum dolore eu feugiat...</p><div class="who">DANA R</div><div class="src">Verified Review</div><div class="line"></div><div class="src-dot"><b></b></div><div class="rated">Rated 5/5</div><div class="stars">★★★★★</div></div>
  <div class="review" style="left:458px"><p>Ut wisi enim ad minim venia quis nostrud exerci tation ullamcorper suscipit lobortis nisl ut aliquip ex ea commodo consequat. Duis autem vel eum ire dolor in hendrerit in vulputate velit esse molesti consequat, vel illum dolore eu feugiat...</p><div class="who">DANA R</div><div class="src">Verified Review</div><div class="line"></div><div class="src-dot"><b></b></div><div class="rated">Rated 5/5</div><div class="stars">★★★★★</div></div>
  <div class="review" style="left:773px"><p>Ut wisi enim ad minim venia quis nostrud exerci tation ullamcorper suscipit lobortis nisl ut aliquip ex ea commodo consequat. Duis autem vel eum ire dolor in hendrerit in vulputate velit esse molesti consequat, vel illum dolore eu feugiat...</p><div class="who">DANA R</div><div class="src">Verified Review</div><div class="line"></div><div class="src-dot"><b></b></div><div class="rated">Rated 5/5</div><div class="stars">★★★★★</div></div>
</section>

<section class="cta" role="img" aria-label="Blue-tinted photo of a home garden lit at night">
  <h2>Ready to Enhance Your Property?</h2>
  <p>Contact us today for a free, no-obligation estimate on irrigation, landscape lighting, or snow removal services.</p>
  <div class="call-btn"><svg width="14" height="14" viewBox="0 0 16 16"><path d="M3 1l3 3-2 2c1 2 3 4 5 5l2-2 3 3-2 3C7 15 1 9 1 3z" fill="none" stroke="#fff" stroke-width="1.4"/></svg>Call Now : (123) 456-7890</div>
</section>

<section class="contact">
  <div class="script">Information</div>
  <h2 class="contact-title">Contact Details</h2>
  <p class="contact-sub">Ut wisi enim ad minim v quis nostrud exerci tat ullamcorper.</p>
  <div class="c-item" style="top:3782px"><div class="c-icon"><svg width="18" height="24" viewBox="0 0 12 16"><path d="M6 0a6 6 0 0 1 6 6c0 4.5-6 10-6 10S0 10.5 0 6a6 6 0 0 1 6-6z" fill="var(--blue)"/><circle cx="6" cy="6" r="2.2" fill="#fff"/></svg></div><h4>Address</h4><span>Ut wisi enim ad minim v qu nostrud exerci tat ullamcorper spit.</span></div>
  <div class="c-item" style="top:3876px"><div class="c-icon"><svg width="24" height="18" viewBox="0 0 24 18"><rect x="1" y="1" width="22" height="16" rx="2" fill="var(--blue)"/><path d="M1 2l11 8 11-8" stroke="#fff" stroke-width="1.6" fill="none"/></svg></div><h4>Email</h4><span>info@willowbrookyards.com</span></div>
  <div class="c-item" style="top:3970px"><div class="c-icon"><svg width="20" height="20" viewBox="0 0 16 16"><path d="M3 1l3 3-2 2c1 2 3 4 5 5l2-2 3 3-2 3C7 15 1 9 1 3z" fill="var(--blue)"/></svg></div><h4>Phone</h4><span>123 456 7890</span></div>

  <div class="form-card">
    <h3>Quick Contact</h3>
    <div class="field" style="top:105px"><label>Name</label><span>Jenna Dowell</span><svg width="11" height="11" viewBox="0 0 12 12"><circle cx="6" cy="3.5" r="3" fill="var(--blue)"/><path d="M0 12c0-4 12-4 12 0z" fill="var(--blue)"/></svg></div>
    <div class="field" style="top:178px"><label>Email</label><span>info@jennadowell.com</span><svg width="12" height="10" viewBox="0 0 12 10"><rect width="12" height="10" rx="1" fill="var(--blue)"/><path d="M0 1l6 4 6-4" stroke="#fff" fill="none"/></svg></div>
    <div class="field" style="top:251px"><label>Phone</label><span>123 456 7890</span><svg width="11" height="11" viewBox="0 0 16 16"><path d="M3 1l3 3-2 2c1 2 3 4 5 5l2-2 3 3-2 3C7 15 1 9 1 3z" fill="var(--blue)"/></svg></div>
    <div class="field" style="top:324px;height:64px"><label>Message</label><span>Enter your message</span><svg width="13" height="11" viewBox="0 0 14 12"><path d="M1 1h12v7H6l-3 3V8H1z" fill="var(--blue)"/></svg></div>
    <div class="btn btn-green" style="left:27px;top:452px;width:186px;height:40px;font-size:12.5px">Get Your Free Estimate</div>
  </div>
</section>

<footer class="footer">
  <div class="f-brand"><div class="brand-dot"></div><div class="brand-name">willowbrook</div></div>
  <div class="f-brand-sub">Landscape &amp; Landscape Lighting &amp; Irrigation</div>
  <p class="f-about">Ut wisi enim ad minim venia, quis nostrud exerci tation ullamcorper suscipit lobortis nisl ut aliquip ex ea commodo consequat. Duis autem vel eum iriure dolor.</p>
  <div class="f-col" style="left:514px"><h5>Quick Links</h5><ul><li>• Home</li><li>• About Us</li><li>• Services</li><li>• Contact Us</li></ul></div>
  <div class="f-col" style="left:726px"><h5>Service Areas</h5><ul><li>• Portland</li><li>• South Portland</li><li>• Scarborough</li><li>• Falmouth</li><li>• Cumberland</li><li>• Surrounding Areas</li></ul></div>
  <div class="f-col f-social" style="left:957px"><h5>Follow Us</h5><ul><li><span class="ico solid"></span>Friendnote</li><li><span class="ico"></span>ClipStream</li><li><span class="ico"></span>Snapgram</li><li><span class="ico"></span>WorkLink</li></ul></div>
  <div class="f-rule"></div>
  <p class="copy">© 2026 Willowbrook Yards. All Rights Reserved.</p>
</footer>

</body>
</html>
```